Real estate agent : TJ Property

I have done the attached logo designed by your company .
My business card description as below:
Name : Daniel Ruiz
Mobile: 0491570156
Email : danielr@tjpropertyhq.net.au
Sales & Property Management

```html
<!DOCTYPE html>
<html lang="en">
<head>
<meta charset="utf-8">
<title>TJ Property – Business Card</title>
<link href="https://fonts.googleapis.com/css2?family=Montserrat:wght@400;600;800&display=swap" rel="stylesheet">
<style>
  :root {
    --ink: #111111;
    --paper: #ffffff;
    --backdrop: #3a3a3c;
    --muted: #2a2a2a;
  }
  * { box-sizing: border-box; margin: 0; padding: 0; }
  html, body {
    width: 1200px; height: 801px; overflow: hidden;
    background: var(--backdrop);
    font-family: "Montserrat", sans-serif;
  }
  .stage {
    width: 1200px; height: 801px;
    display: flex; align-items: center; justify-content: center; gap: 40px;
  }
  .card {
    width: 560px; height: 320px; border-radius: 14px;
    position: relative; overflow: hidden;
    box-shadow: 0 10px 30px rgba(0,0,0,.45);
  }
  /* Back side */
  .card--back { background: var(--ink); display: flex; align-items: center; justify-content: center; }
  .wordmark {
    font-weight: 800; letter-spacing: 2px; text-transform: uppercase; line-height: 1;
    display: flex; align-items: center; gap: 12px;
  }
  .wordmark__dot { width: 14px; height: 14px; }
  .card--back .wordmark { color: var(--paper); font-size: 40px; }
  .card--back .wordmark__dot { background: var(--paper); }

  /* Front side */
  .card--front { background: var(--paper); color: var(--ink); }
  .front__brand {
    position: absolute; left: 28px; top: 0; width: 240px; height: 232px;
    display: flex; align-items: center; justify-content: center;
  }
  .card--front .wordmark { font-size: 30px; color: var(--ink); }
  .card--front .wordmark__dot { background: var(--ink); }
  .front__divider {
    position: absolute; left: 278px; top: 46px; width: 1.5px; height: 150px; background: var(--ink);
  }
  .contact { position: absolute; left: 298px; top: 48px; }
  .contact__name { font-weight: 800; font-size: 24px; text-transform: uppercase; letter-spacing: .3px; }
  .contact__role { font-weight: 400; font-size: 14px; text-transform: uppercase; letter-spacing: .8px; margin-top: 2px; margin-bottom: 14px; }
  .contact__line { display: flex; align-items: center; gap: 7px; font-size: 11.5px; margin-top: 6px; color: var(--muted); }
  .contact__line svg { width: 11px; height: 11px; fill: var(--ink); flex: none; }
  .front__band {
    position: absolute; left: 0; right: 0; bottom: 24px; height: 48px; background: var(--ink);
    color: var(--paper); display: flex; align-items: center; justify-content: center;
    font-weight: 800; font-size: 15px; letter-spacing: 1.5px; text-transform: uppercase;
  }
</style>
</head>
<body>
<main class="stage">
  <section class="card card--back" aria-label="Card back">
    <div class="wordmark"><span class="wordmark__dot"></span>TJ Property</div>
  </section>

  <section class="card card--front" aria-label="Card front">
    <div class="front__brand">
      <div class="wordmark"><span class="wordmark__dot"></span>TJ Property</div>
    </div>
    <div class="front__divider"></div>
    <div class="contact">
      <h1 class="contact__name">Daniel Ruiz</h1>
      <p class="contact__role">Real Estate Agent</p>
      <p class="contact__line">
        <svg viewBox="0 0 24 24"><path d="M6.6 10.8a15.1 15.1 0 0 0 6.6 6.6l2.2-2.2a1 1 0 0 1 1-.25 11.4 11.4 0 0 0 3.6.57 1 1 0 0 1 1 1V20a1 1 0 0 1-1 1A17 17 0 0 1 3 4a1 1 0 0 1 1-1h3.5a1 1 0 0 1 1 1c0 1.25.2 2.45.57 3.57a1 1 0 0 1-.25 1z"/></svg>
        0491570156
      </p>
      <p class="contact__line">
        <svg viewBox="0 0 24 24"><path d="M2 5h20v14H2z M2 5l10 8 10-8" fill="none" stroke="#111" stroke-width="2.4"/></svg>
        danielr@tjpropertyhq.net.au
      </p>
      <p class="contact__line">
        <svg viewBox="0 0 24 24"><circle cx="12" cy="12" r="10" fill="none" stroke="#111" stroke-width="2"/><path d="M2 12h20M12 2c3 3 3 17 0 20M12 2c-3 3-3 17 0 20" fill="none" stroke="#111" stroke-width="1.6"/></svg>
        www.tjpropertyhq.net.au
      </p>
    </div>
    <div class="front__band">Sales &amp; Property Management</div>
  </section>
</main>
</body>
</html>
```